User help guide for software for investment bank

We need a professional design for our user help guides for new software we have written for our client. We develop visualization software for investment banks in Singapore mainly focused in the financial and risk management area. Our help guides are design to show them how the software works as well as promote our brand
Updates

Project Deadline Extended Reason: I am looking for more alternative designs and we have around 10 more documents to do after this Added Saturday, November 21, 2015

Target Market(s)

Investment banking, risk management, finance

Industry/Entity Type

Bank

Requirements
Must have
• Content of document and logos
• Colour sheme
• Professional brouchure design
• Quorvin and bimsot logos on it
• Look at www.quorvin-example.com for company looks and feel
• PLEASE USE COLOUR SCHEMES BELOW IN ATTACHMENT AND FOLLOW SIMILAR STYLE TO CLIENT ANNUAL REPORT

```html
<!DOCTYPE html>
<html lang="en">
<head>
<meta charset="utf-8">
<title>User Roles and Permissions – Help Guide</title>
<link rel="stylesheet" href="https://fonts.googleapis.com/css2?family=Archivo:wght@800&family=Roboto:wght@300;400;500;700&display=swap">
<style>
:root{
  --bg:#8d8d8d;
  --paper:#ffffff;
  --blue:#1a6cad;
  --green:#5bb947;
  --panel:#dbe6f3;
  --ink:#1b1b1b;
  --body:#333333;
  --rule:#8a8a8a;
  --cell-line:#ffffff;
}
*{box-sizing:border-box;margin:0;padding:0}
html,body{width:1033px;height:1200px;overflow:hidden;background:var(--bg)}
body{font-family:"Roboto",Arial,sans-serif;color:var(--body)}
.page{position:absolute;left:106px;top:20px;width:820px;height:1160px;background:var(--paper)}
.block{position:absolute;left:63px;width:702px}
.section-title{font-family:"Archivo","Arial Black",sans-serif;font-weight:800;font-size:25px;color:var(--blue);letter-spacing:.1px;line-height:1}
.rule{position:absolute;left:63px;width:702px;height:2px;background:var(--rule)}
.rule.thin{height:1px;background:#b9b9b9}
.panel{position:absolute;left:63px;top:132px;width:702px;height:397px;background:var(--panel);padding:14px 24px 0 24px}
.panel-intro{font-size:13.6px;font-weight:500;color:var(--ink);line-height:17px}
.panel-intro em{font-style:normal;color:var(--blue)}
.panel-rule{height:1px;background:#9aa4b0;margin:9px 0 12px}
.roles{display:flex;font-size:13.6px;line-height:21px}
.roles .col{width:267px}
.roles .col+.col{width:400px}
.role-name{color:var(--green);font-weight:700}
.roles p{font-weight:300;color:var(--ink)}
.roles p::before{content:"• ";color:var(--green);font-weight:700}
.perm-table{position:absolute;left:24px;top:179px;width:658px;border-collapse:collapse;font-size:13.6px}
.perm-table th{background:var(--green);color:#fff;font-weight:700;height:68px;line-height:16px;border:2px solid var(--cell-line);padding:0 10px}
.perm-table td{height:40px;border:2px solid var(--cell-line);text-align:center;font-weight:300;color:var(--ink)}
.perm-table td:first-child{text-align:left;padding-left:8px}
.perm-table th:first-child{width:148px}
.intro{font-size:13.6px;font-weight:500;color:var(--ink);line-height:17px}
.list-head{font-size:13.6px;font-weight:700;color:var(--blue);margin-bottom:6px}
.list-head span{color:var(--green)}
.bullets{list-style:none;font-size:13.6px;font-weight:300;color:var(--ink);line-height:16.5px}
.bullets li{margin-bottom:5.5px}
.bullets li::before{content:"• ";color:var(--blue);font-weight:700}
.col-left{position:absolute;left:63px;top:744px;width:340px}
.col-right{position:absolute;left:428px;top:744px;width:337px}
.photo{position:absolute;left:428px;top:892px;width:337px;height:184px;background:linear-gradient(160deg,#48563c 0%,#2a3324 55%,#1d2230 100%)}
.page-num{position:absolute;right:55px;top:1110px;font-size:12.5px;font-weight:700;color:#8a8a8a}
</style>
</head>
<body>
<main class="page">
  <h1 class="block section-title" style="top:61px">1. User Roles and Permissions</h1>
  <div class="rule" style="top:105px"></div>

  <section class="panel">
    <p class="panel-intro">The Web Editor Tool is allowed to be used to all the users that have <em>edit permissions</em> in their user role. Currently, KRMT tool has the roles below:</p>
    <div class="panel-rule"></div>
    <div class="roles">
      <div class="col">
        <div class="role-name">Risk Administrator:</div>
        <p>Can do everything into Quorvin model</p>
        <div class="role-name">Risk Administrator:</div>
        <p>Can do everything into Quorvin model</p>
      </div>
      <div class="col">
        <div class="role-name">Risk Project Leader:</div>
        <p>He can modify the report but NOT saving it or create a new one</p>
        <p>He cannot move or delete the current reports stored at server</p>
      </div>
    </div>
    <table class="perm-table">
      <thead>
        <tr><th>User Name</th><th>Can access to<br>Web Edit Tool</th><th>Can modify the<br>current report but<br>no saving this</th><th>Can create new<br>reports or modify<br>the current ones</th></tr>
      </thead>
      <tbody>
        <tr><td>Risk Administrator</td><td>YES</td><td>N/A</td><td>YES</td></tr>
        <tr><td>Risk Project Leader</td><td>YES</td><td>YES</td><td>NO</td></tr>
        <tr><td>Risk Publisher</td><td>NO</td><td>NO</td><td>NO</td></tr>
      </tbody>
    </table>
  </section>

  <h2 class="block section-title" style="top:589px">2. Restrictions using Web Editor Tool</h2>
  <div class="rule" style="top:634px"></div>
  <p class="block intro" style="top:663px">Web Editor Tool contains big part of the current functionalities included at Quorvin Desktop. This allows to the users to modify or create new reports online, without using Quorvin Desktop. There are some rules that the users must bear in mind using the Web Editor Tool:</p>
  <div class="rule thin" style="top:718px"></div>

  <div class="col-left">
    <h3 class="list-head">What the Web Editor Tool users <span>CAN</span> do:</h3>
    <ul class="bullets">
      <li>Create new views (sheets), duplicate, and rename views in a workbook</li>
      <li>Change aggregation of measures</li>
      <li>Use Show me to create views</li>
      <li>View underlying data</li>
      <li>Create and edit calculated fields, and use quick table calculations</li>
      <li>Drag field to different mark types in the Marks card</li>
      <li>Use the Analytics pane to drag reference lines, trend lines, and other objects into the view</li>
      <li>Add, modify, and remove filters (Shown as Quick Filters), and edit a filter layout.</li>
      <li>Show labels, totals and subtotals</li>
      <li>Swap X and Y axes</li>
      <li>Change the view size</li>
      <li>Exclude or remove fields in the view</li>
    </ul>
  </div>

  <div class="col-right">
    <h3 class="list-head">What the Web Editor Tool users <span>CANNOT</span> do:</h3>
    <ul class="bullets">
      <li>Cannot add data sources to a published workbook</li>
      <li>Data model editing is not supported</li>
      <li>Dashboards and stories cannot be created or modified at the server</li>
      <li>Formatting options are not available</li>
    </ul>
  </div>

  <div class="photo" role="img" aria-label="Photo of a person outdoors at dusk holding a tablet showing a data dashboard"></div>

  <div class="rule" style="top:1103px"></div>
  <div class="page-num">3</div>
</main>
</body>
</html>
```